Web design for sitter site

We will be launching a sitter site in the coming months that focuses on sitters for children. The name of this site will be KinWatch.com
We will need:
1. main page design
2. site logo designed
3. subpages as well for the look of people's profiles, and job listings, etc (see links below)
We only need the design, photos, font files, etc. We do not need this site coded (no html), a ps job is fine.
Some competing sites in the space include - tendhaven.com and mindly.com
http://www.example-guardia.com/images/profile1.jpg
http://brookvaleshelf.example/wp-content/uploads/2013/09/mindly-review.png
http://www.pinecrestuni.example/hr/photos/tend_haven2.jpg
Thanks for your interest!
Target Market(s)
Mothers of children, mainly women
Industry/Entity Type
Online
Look and feel

```html
<!DOCTYPE html>
<html lang="en">
<head>
<meta charset="utf-8">
<title>KinWatch.com</title>
<link href="https://fonts.googleapis.com/css2?family=Source+Sans+3:wght@400;600;700&display=swap" rel="stylesheet">
<style>
:root{
  --ink:#1c2333;
  --red:#d63d2e;
  --teal:#23918a;
  --teal-dark:#1f7a6f;
  --mist:#e0ebe6;
  --white:#ffffff;
  --grey:#8a8f94;
  --line:#e2e4e6;
}
*{margin:0;padding:0;box-sizing:border-box}
html,body{width:874px;height:1200px;overflow:hidden}
body{position:relative;background:var(--mist);font-family:"Source Sans 3",sans-serif;color:var(--grey)}
.abs{position:absolute}
.topbar{left:0;top:0;width:874px;height:102px;background:var(--ink)}
.utility{right:152px;top:21px;display:flex;align-items:center;gap:7px;font-size:8.5px;text-transform:uppercase;color:var(--white)}
.utility .accent{color:var(--red)}
.country{border:1px solid #cfd3d8;padding:2px 8px;width:67px;height:15px;display:flex;justify-content:space-between;align-items:center;margin-right:22px}
.country svg{width:7px;height:6px}
.nav{left:138px;top:50px;width:599px;height:52px;background:var(--red);display:flex}
.nav a{display:flex;align-items:center;justify-content:center;width:62px;color:var(--white);font-size:8.5px;text-transform:uppercase;text-decoration:none;border-right:1px solid #c23527}
.nav a.current{background:var(--mist);color:var(--ink)}
.login{left:635px;top:69px;width:69px;height:21px;background:var(--mist);border-radius:3px;color:var(--ink);font-size:11px;display:flex;align-items:center;justify-content:center}
.band{left:0;top:102px;width:874px;height:294px;background:var(--teal)}
.brand{left:140px;top:128px;font-size:22px;font-weight:700;color:var(--white);letter-spacing:.3px}
.social{left:619px;top:132px;display:flex;gap:12px}
.social span{width:20px;height:20px;border-radius:50%;background:#5cb8b0;display:block}
.hero{left:138px;top:178px;width:599px;height:212px;border:2px solid #eef2f1;background:linear-gradient(90deg,#c9a48a 0%,#e2c3ac 45%,#f6f4f2 70%,#fafafa 100%)}
.slogan{left:540px;top:258px;width:196px;height:36px;background:var(--ink);color:var(--white);font-size:18px;display:flex;align-items:center;padding-left:21px}
.slogan.sub{left:588px;top:296px;width:148px;height:34px;background:#dcdfe1;color:var(--ink);font-size:15px;padding-left:11px}
.dots{left:691px;top:376px;display:flex;gap:3px}
.dots i{width:4px;height:3px;background:#cfd3d6;display:block}
.dots i:first-child{background:var(--red)}
.card{background:var(--white)}
.welcome{left:138px;top:402px;width:405px;height:173px;padding:26px 19px}
.welcome h1{font-size:19px;font-weight:400;color:var(--red)}
.welcome h2{font-size:11.5px;font-weight:400;color:var(--teal-dark);margin:6px 0 6px}
.welcome p{font-size:7.6px;line-height:12.4px}
.btn{display:inline-block;background:var(--teal-dark);color:var(--white);font-size:7px;padding:5px 5px;text-transform:uppercase}
.welcome .btn{margin-top:19px}
.feature{top:594px;width:193px;height:378px;padding:22px 17px}
.feature h3{font-size:15px;font-weight:700;color:var(--red);text-transform:uppercase;margin-left:-1px}
.feature .photo{width:157px;height:112px;margin:15px 0 14px}
.feature h4{font-size:11px;font-weight:400;color:var(--teal-dark);text-transform:uppercase;margin-bottom:9px}
.feature p{font-size:8px;line-height:15px}
.feature .btn{margin-top:18px}
.finder{left:562px;top:403px;width:175px;height:82px;background:var(--red);padding:16px 13px}
.finder h5{font-size:10.5px;font-weight:700;color:var(--white);text-transform:uppercase}
.search{margin-top:9px;height:22px;background:var(--white);display:flex;justify-content:flex-end;align-items:center;padding-right:6px}
.how{left:562px;top:485px;width:175px;height:173px;padding:22px 13px}
.heading{display:flex;align-items:center;gap:8px;font-size:10.5px;color:var(--red);text-transform:uppercase;margin-bottom:10px}
.how ul{list-style:none}
.how li{font-size:7px;padding:6px 0 6px;border-bottom:1px solid var(--line)}
.how li:last-child{border:none}
.match{left:562px;top:678px;width:175px;height:294px;padding:22px 13px}
.person{display:flex;gap:12px;margin-bottom:25px}
.person .thumb{width:56px;height:56px;flex:none}
.person p{font-size:7px;line-height:11px}
.person a{display:block;font-size:7px;color:var(--teal-dark);margin-top:13px;text-decoration:none}
.footer{left:0;top:990px;width:874px;height:174px;background:var(--ink)}
.foot-col h6{font-size:11px;font-weight:400;color:var(--white);text-transform:uppercase}
.nav-links{left:138px;top:1020px}
.nav-links ul{list-style:none;margin-top:12px}
.nav-links li{font-size:7.5px;color:#555d6b;line-height:15px;padding-left:2px}
.services{left:325px;top:1020px;width:187px}
.services ul{list-style:none;margin-top:8px}
.services li{display:flex;align-items:center;gap:9px;font-size:7.5px;color:#555d6b;height:25px;border-bottom:1px solid #2e3645}
.services li:last-child{border:none}
.findus{left:546px;top:1020px;width:190px}
.findus h6{margin-left:26px}
.findus p{font-size:8px;color:var(--teal);line-height:12.5px;margin-top:8px}
.phone{display:flex;align-items:center;gap:6px;margin-top:18px;font-size:16px;font-weight:700;color:var(--red);margin-left:4px}
.legal{left:0;top:1164px;width:874px;height:36px;background:var(--teal);color:var(--white);font-size:7px;text-align:center;line-height:30px}
</style>
</head>
<body>
<header class="abs topbar"></header>
<div class="abs utility">
  <span class="accent">Change country</span>
  <span class="country">Canada <svg viewBox="0 0 7 6"><path d="M0 0h7L3.5 6z" fill="#d63d2e"/></svg></span>
  <span class="accent">Sign up</span>&nbsp;<span>Parents</span> | <span>Sitters</span>
</div>
<nav class="abs nav">
  <a class="current">Home</a><a>About us</a><a>Services</a><a>Finder</a><a>Child nanny</a><a>Housekeeper</a>
</nav>
<div class="abs login">LOGIN</div>

<section class="abs band"></section>
<div class="abs brand">KINWATCH.COM</div>
<div class="abs social"><span></span><span></span><span></span><span></span></div>
<div class="abs hero" role="img" aria-label="Smiling family of parents with two children"></div>
<div class="abs slogan">HELPING PARENTS</div>
<div class="abs slogan sub">FIND BABYSITTERS</div>
<div class="abs dots"><i></i><i></i><i></i><i></i></div>

<section class="abs card welcome">
  <h1>WELCOME</h1>
  <h2>Proin nunc ante, tempus ac porta blandit.</h2>
  <p>Ut mollis blandit mi, vel ultricies arcu iaculis in. Vestibulum pellentesque volutpat sem quis mattis. Morbi egestas suscipit sem ut lacinia. Morbi interdum, orci et lacinia lacinia, nibh sapien blandit leo, a ornare lectus nulla in urna mauris, quis hendrerit mi hendrerit quis. Lorem ipsu.</p>
  <span class="btn">More info</span>
</section>

<section class="abs card feature" style="left:138px">
  <h3>Sitters for children</h3>
  <div class="photo" role="img" aria-label="Mother holding a smiling toddler" style="background:linear-gradient(135deg,#b98a5e,#e6c3a0 60%,#8fb07a)"></div>
  <h4>Nam iaculis fermentum</h4>
  <p>Trices lacinia sem interdum vitae. Suspendisse a urna id nulla hendrerit porttitor ultrices in odio. Vivamus varius, arcu id vestibulum sagittis, lorem<br>Trices lacinia sem interdum vitae. Suspendisse a urna id nulla hendrerit porttitor ultrices in odio. Vivamus varius, arcu id vestibulum sagittis, lorem</p>
  <span class="btn">More info</span>
</section>

<section class="abs card feature" style="left:350px">
  <h3>Pet's</h3>
  <div class="photo" role="img" aria-label="Black dog with a veterinarian" style="background:linear-gradient(90deg,#222428 0%,#3a3c40 45%,#dfe6ea 70%,#f2f4f5)"></div>
  <h4>Nam iaculis fermentum</h4>
  <p>Trices lacinia sem interdum vitae. Suspendisse a urna id nulla hendrerit porttitor ultrices in odio. Vivamus varius, arcu id vestibulum sagittis, lorem<br>Trices lacinia sem interdum vitae. Suspendisse a urna id nulla hendrerit porttitor ultrices in odio. Vivamus varius, arcu id vestibulum sagittis, lorem</p>
  <span class="btn">More info</span>
</section>

<aside class="abs finder">
  <h5>Finder job / care</h5>
  <div class="search"><svg width="11" height="11" viewBox="0 0 11 11"><circle cx="4.3" cy="4.3" r="3.2" fill="none" stroke="#1f7a6f" stroke-width="1.6"/><path d="M6.6 6.6L10 10" stroke="#1f7a6f" stroke-width="2"/></svg></div>
</aside>
<aside class="abs card how">
  <div class="heading"><svg width="12" height="12" viewBox="0 0 12 12"><circle cx="6" cy="6" r="3.6" fill="none" stroke="#23918a" stroke-width="2.4" stroke-dasharray="1.8 1"/><circle cx="6" cy="6" r="1.4" fill="#23918a"/></svg>See how it works</div>
  <ul>
    <li>In ut leo eu mi rutrum pellentesque</li>
    <li>Maecenas consequat eleifend ligula</li>
    <li>Aenean nec ipsum turpis id vestibulum</li>
    <li>Proin at mauris at odio vulputate accu</li>
    <li>Mauris condimentum cursus tortor sit</li>
  </ul>
</aside>
<aside class="abs card match">
  <div class="heading"><svg width="11" height="11" viewBox="0 0 11 11"><path d="M1 10l1-3 6-6 2 2-6 6z" fill="#1f7a6f"/></svg>Find the right match</div>
  <div class="person"><div class="thumb" role="img" aria-label="Portrait of a sitter" style="background:linear-gradient(#e7e3df,#c9a58c)"></div><div><p>Phasellus scelerisque enim eget eros accum san eget ullamco</p><a>More info +</a></div></div>
  <div class="person"><div class="thumb" role="img" aria-label="Portrait of a sitter" style="background:linear-gradient(#eceae8,#b79a88)"></div><div><p>Phasellus scelerisque enim eget eros accum san eget ullamco</p><a>More info +</a></div></div>
  <div class="person"><div class="thumb" role="img" aria-label="Portrait of a sitter" style="background:linear-gradient(#efe9e4,#d7a98a)"></div><div><p>Phasellus scelerisque enim eget eros accum san eget ullamco</p><a>More info +</a></div></div>
</aside>

<footer class="abs footer"></footer>
<div class="abs foot-col nav-links">
  <h6>Navigation</h6>
  <ul><li>About Us</li><li>Investor Relations</li><li>Maple's Blog</li><li>Help</li><li>Privacy Policy</li><li>Careers</li></ul>
</div>
<div class="abs foot-col services">
  <h6>More services</h6>
  <ul>
    <li><svg width="9" height="7" viewBox="0 0 9 7"><path d="M0 2.5h5V0l4 3.5L5 7V4.5H0z" fill="#d63d2e"/></svg>Duis quis dolor felis, aliquet blandit lipsum</li>
    <li><svg width="9" height="7" viewBox="0 0 9 7"><path d="M0 2.5h5V0l4 3.5L5 7V4.5H0z" fill="#d63d2e"/></svg>Phasellus sed erat augue, non porta untun</li>
    <li><svg width="9" height="7" viewBox="0 0 9 7"><path d="M0 2.5h5V0l4 3.5L5 7V4.5H0z" fill="#d63d2e"/></svg>Nullam non erat et nisl mattis mollis in unoki</li>
    <li><svg width="9" height="7" viewBox="0 0 9 7"><path d="M0 2.5h5V0l4 3.5L5 7V4.5H0z" fill="#d63d2e"/></svg>Maecenas at ipsum vel eros auctor fausino</li>
  </ul>
</div>
<div class="abs foot-col findus">
  <h6>Find us on</h6>
  <p>Sed neque lectus, blandit tempor eleifend ut, lacinia vitae sapien porta pulvin fuse sapien.</p>
  <div class="phone"><svg width="26" height="18" viewBox="0 0 26 18"><path d="M2 6c0-3 5-5 11-5s11 2 11 5l-4 1-1-3H7L6 7z" fill="#d63d2e"/><path d="M6 8h14l3 9H3z" fill="#d63d2e"/><circle cx="13" cy="12.5" r="2.5" fill="#1c2333"/></svg>(000) 555 01234</div>
</div>
<div class="abs legal">Copyright © 2014 kinwatch.com. All Rights Reserved.</div>
</body>
</html>
```